Book cover for book about Climate Change

Looking for a clean, bold, and attractive cover for a mass-market paperback (5.5"x 8.5") about solving the climate change problem. Title is either "When Rivers Learn to Sing” or A Lantern Over Quiet Fields” (your choice), subtitle is "A five-step plan to reverse climate change — to ensure that your grandchildren will live on a clean and comfortable planet," author is Dale Pruitt. Thinking that it *might* feature an image of Earth (or a portion thereof) and its very thin layer of atmosphere -- but STRONGLY encourage other ideas too!

Requirements
Nice to have
• Keep it positive — NOT scary doom-and-gloom

```html
<!DOCTYPE html>
<html lang="en">
<head>
<meta charset="utf-8">
<title>When Rivers Learn to Sing — Dale Pruitt</title>
<link rel="stylesheet" href="https://fonts.googleapis.com/css2?family=Open+Sans:wght@400;600;800&display=swap">
<style>
  :root {
    --space-deep: #02040c;
    --space-mid: #0a1632;
    --ink-white: #ffffff;
    --ink-soft: #e8eef8;
    --glow-blue: rgba(120, 180, 255, 0.75);
  }
  * { margin: 0; padding: 0; box-sizing: border-box; }
  html, body { width: 841px; height: 1200px; overflow: hidden; background: var(--space-deep); }
  .cover {
    position: relative;
    width: 841px;
    height: 1200px;
    overflow: hidden;
    background: radial-gradient(ellipse at 60% 35%, var(--space-mid) 0%, var(--space-deep) 65%);
    font-family: "Open Sans", Arial, sans-serif;
    color: var(--ink-white);
    text-align: center;
  }
  .planet-art {
    position: absolute;
    left: 0; top: 0;
    width: 841px; height: 760px;
  }
  .author {
    position: absolute;
    top: 26px; left: 0; right: 0;
    font-size: 34px;
    font-weight: 400;
    letter-spacing: 8px;
  }
  .title {
    position: absolute;
    top: 600px; left: 0; right: 0;
    line-height: 1;
  }
  .title-lead {
    display: block;
    font-size: 54px;
    font-weight: 400;
  }
  .title-middle {
    display: block;
    margin-top: 22px;
    font-size: 78px;
    font-weight: 400;
    letter-spacing: 10px;
  }
  .title-key {
    display: block;
    margin-top: 10px;
    font-size: 196px;
    font-weight: 800;
    letter-spacing: 4px;
    text-shadow: 0 0 28px var(--glow-blue), 0 0 60px rgba(90, 150, 255, 0.45);
  }
  .subtitle {
    position: absolute;
    top: 1000px; left: 60px; right: 60px;
    font-size: 28px;
    font-weight: 400;
    line-height: 1.45;
    color: var(--ink-soft);
  }
</style>
</head>
<body>
  <main class="cover">
    <svg class="planet-art" viewBox="0 0 841 760" role="img" aria-label="Earth seen from space with blue oceans, white clouds and a thin glowing atmosphere against a starry sky">
      <defs>
        <radialGradient id="planetFill" cx="0.42" cy="0.62" r="0.75">
          <stop offset="0" stop-color="#7fb6f0"/>
          <stop offset="0.35" stop-color="#2f6fc0"/>
          <stop offset="0.7" stop-color="#123a7a"/>
          <stop offset="1" stop-color="#050d22"/>
        </radialGradient>
        <radialGradient id="atmosphere" cx="0.5" cy="0.5" r="0.5">
          <stop offset="0.86" stop-color="#6fb0ff" stop-opacity="0"/>
          <stop offset="0.93" stop-color="#8cc4ff" stop-opacity="0.55"/>
          <stop offset="1" stop-color="#4a8de8" stop-opacity="0"/>
        </radialGradient>
      </defs>
      <circle cx="590" cy="390" r="370" fill="url(#atmosphere)"/>
      <circle cx="590" cy="390" r="330" fill="url(#planetFill)"/>
    </svg>

    <p class="author">DALE PRUITT</p>

    <h1 class="title">
      <span class="title-lead">When Rivers</span>
      <span class="title-middle">LEARN TO</span>
      <span class="title-key">SING</span>
    </h1>

    <p class="subtitle">A five-step plan to reverse climate change - to ensure that your grandchildren will live on a clean and comfortable planet</p>
  </main>
</body>
</html>
```